Industrial automation company needs new business cards

We need a new business card designed. We have an existing logo that is very simple and are happy to consider changes to it. We have been in business for more than 10 years and our logo has some brand recognition.
We are a company of engineers and build systems for industrial automation, substation automation, power and energy monitoring and production data vertical integration. Our main clients are food manufacturers, data centers and government establishments.
Our current business cards have our name, qualifications, job title, telephone, email and web address details. We don't need our physical address on our business cards. I've attached our current logo

Industry/Entity Type

Business

Logo Text

varlo

Font styles to use
Sans Serif

Colors
6b449b

Requirements
Must have
• - double sided business cards
• - name (eg Hello There)
• - qualifications (BE Elec MIRQT)
• - job title (eg Senior Engineer)
• - telephone (eg 0412 555 019)
• - email (eg hello.there@varlo.com.au)
• - web address (eg varlo.com.au)
Nice to have
• include our target markets on the back side of the card
• - industrial automation
• - substation automation
• - power and energy monitoring
• - production data vertical integration

```html
<!DOCTYPE html>
<html lang="en">
<head>
<meta charset="utf-8">
<title>Varlo business cards</title>
<link rel="stylesheet" href="https://fonts.googleapis.com/css2?family=Lato:wght@400;700;900&display=swap">
<style>
  :root {
    --brand-purple: #6b449b;
    --card-white: #ffffff;
    --swoosh-grey: #a7a9ac;
    --page-bg: #2b2b2d;
    --ink-grey: #6d6e71;
  }
  * { box-sizing: border-box; margin: 0; padding: 0; }
  html, body { width: 1200px; height: 880px; overflow: hidden; }
  body {
    background: var(--page-bg);
    font-family: "Lato", sans-serif;
    position: relative;
  }
  .card {
    position: absolute;
    left: 260px;
    width: 680px;
    height: 388px;
    border-radius: 26px;
    overflow: hidden;
  }
  .card-front { top: 36px; background: var(--brand-purple); color: var(--card-white); }
  .card-back { top: 456px; background: var(--card-white); }

  .brand { display: flex; align-items: center; gap: 14px; }
  .brand-mark { border-radius: 50%; flex: none; }
  .brand-name {
    font-weight: 700;
    letter-spacing: 9px;
    line-height: 1;
  }
  .card-front .brand { position: absolute; left: 150px; top: 110px; }
  .card-front .brand-mark { width: 70px; height: 70px; background: var(--card-white); }
  .card-front .brand-name { font-size: 64px; }
  .markets {
    position: absolute;
    left: 0; right: 0;
    top: 230px;
    text-align: center;
    font-size: 17px;
    line-height: 1.35;
    letter-spacing: 0.3px;
  }

  .back-shape { position: absolute; inset: 0; }
  .person {
    position: absolute;
    right: 40px;
    top: 60px;
    text-align: right;
    color: var(--card-white);
    line-height: 1.2;
  }
  .person-name { font-weight: 900; font-size: 22px; letter-spacing: 0.5px; }
  .person-quals { font-weight: 700; font-size: 16px; }
  .person-title { font-size: 16px; }
  .card-back .brand { position: absolute; left: 56px; top: 186px; color: var(--brand-purple); }
  .card-back .brand-mark { width: 60px; height: 60px; background: var(--brand-purple); }
  .card-back .brand-name { font-size: 54px; }
  .social-dot {
    position: absolute;
    right: 34px;
    top: 262px;
    width: 24px; height: 24px;
    border: 2px solid var(--brand-purple);
    border-radius: 50%;
  }
  .contacts {
    position: absolute;
    left: 56px;
    bottom: 30px;
    list-style: none;
    color: var(--ink-grey);
    font-size: 17px;
    line-height: 1.2;
  }
  .contacts li { display: flex; align-items: center; gap: 10px; margin-top: 6px; }
  .contact-icon { width: 20px; height: 20px; flex: none; }
</style>
</head>
<body>

<section class="card card-front" aria-label="Card front">
  <div class="brand">
    <span class="brand-mark"></span>
    <span class="brand-name">VARLO</span>
  </div>
  <p class="markets">
    industrial automation | substation automation | power and energy monitoring<br>
    production data vertical integration
  </p>
</section>

<section class="card card-back" aria-label="Card back">
  <svg class="back-shape" viewBox="0 0 680 388" width="680" height="388" aria-hidden="true">
    <path d="M0,0 H680 V170 C470,128 220,128 0,62 Z" fill="var(--brand-purple)"/>
    <path d="M0,62 C220,128 470,128 680,170 V186 C470,142 220,142 0,70 Z" fill="var(--swoosh-grey)"/>
  </svg>

  <div class="person">
    <p class="person-name">BEN CARTER</p>
    <p class="person-quals">(BE Elec MIRQT)</p>
    <p class="person-title">Senior Engineer</p>
  </div>

  <span class="social-dot"></span>

  <div class="brand">
    <span class="brand-mark"></span>
    <span class="brand-name">VARLO</span>
  </div>

  <ul class="contacts">
    <li>
      <svg class="contact-icon" viewBox="0 0 20 20" aria-hidden="true">
        <circle cx="10" cy="10" r="10" fill="var(--brand-purple)"/>
        <path d="M6 5.5c0 5 3.5 8.5 8.5 8.5l1-2-2.5-1.2-1 1c-1.5-.6-2.7-1.8-3.3-3.3l1-1L8.5 5 6 5.5z" fill="#fff"/>
      </svg>
      0412 555 019
    </li>
    <li>
      <svg class="contact-icon" viewBox="0 0 20 20" aria-hidden="true">
        <circle cx="10" cy="10" r="10" fill="var(--brand-purple)"/>
        <rect x="5" y="6.5" width="10" height="7" fill="none" stroke="#fff" stroke-width="1.3"/>
        <path d="M5 6.5l5 4 5-4" fill="none" stroke="#fff" stroke-width="1.3"/>
      </svg>
      hello.there@varlo.com.au
    </li>
    <li>
      <svg class="contact-icon" viewBox="0 0 20 20" aria-hidden="true">
        <circle cx="10" cy="10" r="10" fill="var(--brand-purple)"/>
        <circle cx="10" cy="10" r="5.5" fill="none" stroke="#fff" stroke-width="1.2"/>
        <ellipse cx="10" cy="10" rx="2.4" ry="5.5" fill="none" stroke="#fff" stroke-width="1.2"/>
        <path d="M4.5 10h11" stroke="#fff" stroke-width="1.2"/>
      </svg>
      www.varlo.com.au
    </li>
  </ul>
</section>

</body>
</html>
```